Building Company Business Card Design

I am looking to get a business card designed for my Building Company. Please find the logo attached.

Industry/Entity Type

Business

Contact Information for Business Card

Mobile 0472 913 046
Email admin@tarrowconstructworks.com.au
Website www.tarrowconstructworks.com.au

Colors
0255a3

```html
<!DOCTYPE html>
<html lang="en">
<head>
<meta charset="utf-8">
<title>Tarrow Construct Works – Business Card</title>
<link href="https://fonts.googleapis.com/css2?family=Montserrat:wght@400;500;700&display=swap" rel="stylesheet">
<style>
  :root {
    --brand-blue: #0255a3;
    --brand-blue-deep: #013f7d;
    --brand-blue-light: #2a78c4;
    --paper: #f4f4f3;
    --backdrop: #dcdcdc;
    --ink: #222426;
    --grey: #6d6f72;
  }
  * { box-sizing: border-box; margin: 0; padding: 0; }
  html, body {
    width: 1200px; height: 874px; overflow: hidden;
    background: var(--backdrop);
    font-family: "Montserrat", sans-serif;
  }
  .canvas {
    position: relative; width: 1200px; height: 874px;
  }
  .card {
    position: absolute; left: 320px; width: 560px; height: 320px;
    background: var(--paper); overflow: hidden;
    box-shadow: 0 2px 6px rgba(0,0,0,0.12);
  }
  .card--front { top: 92px; }
  .card--back { top: 462px; }
  .card__shape { position: absolute; inset: 0; width: 100%; height: 100%; }

  .wordmark {
    position: absolute; font-weight: 700; letter-spacing: 1px;
    line-height: 1.05; text-transform: uppercase;
  }
  .card--front .wordmark {
    left: 44px; top: 92px; font-size: 30px; color: var(--brand-blue);
  }
  .card--back .wordmark {
    left: 32px; top: 48px; font-size: 17px; color: #ffffff;
  }
  .front__web {
    position: absolute; right: 34px; bottom: 30px;
    color: #ffffff; font-size: 13px; font-weight: 500; letter-spacing: 0.3px;
  }

  .person { position: absolute; left: 330px; top: 92px; }
  .person__name {
    font-size: 19px; font-weight: 700; color: var(--brand-blue); letter-spacing: 0.5px;
  }
  .person__role { font-size: 15px; color: var(--ink); margin-top: 2px; }

  .contacts {
    position: absolute; left: 186px; top: 204px; list-style: none;
  }
  .contacts__item {
    display: flex; align-items: center; gap: 10px;
    font-size: 15.5px; color: var(--ink); height: 26px;
  }
  .contacts__icon {
    width: 17px; height: 17px; border-radius: 50%;
    background: var(--brand-blue); flex: none;
    display: flex; align-items: center; justify-content: center;
  }
  .contacts__icon svg { width: 11px; height: 11px; }
</style>
</head>
<body>
<main class="canvas">

  <section class="card card--front" aria-label="Business card front">
    <svg class="card__shape" viewBox="0 0 560 320" preserveAspectRatio="none" aria-hidden="true">
      <defs>
        <linearGradient id="frontSwoosh" x1="0" y1="1" x2="1" y2="0">
          <stop offset="0" stop-color="var(--brand-blue-deep)"/>
          <stop offset="1" stop-color="var(--brand-blue-light)"/>
        </linearGradient>
      </defs>
      <path d="M0,320 C220,300 460,200 560,0 L560,320 Z" fill="url(#frontSwoosh)"/>
      <path d="M30,320 C250,296 470,180 560,50 L560,320 Z" fill="var(--brand-blue)"/>
      <path d="M60,320 C280,296 480,200 560,110 L560,320 Z" fill="var(--brand-blue)" opacity="0.85"/>
    </svg>
    <div class="wordmark">Tarrow<br>Construct Works</div>
    <div class="front__web">tarrowconstructworks.com.au</div>
  </section>

  <section class="card card--back" aria-label="Business card back">
    <svg class="card__shape" viewBox="0 0 560 320" preserveAspectRatio="none" aria-hidden="true">
      <defs>
        <linearGradient id="backSwoosh" x1="0" y1="0" x2="1" y2="1">
          <stop offset="0" stop-color="var(--brand-blue-light)"/>
          <stop offset="1" stop-color="var(--brand-blue-deep)"/>
        </linearGradient>
      </defs>
      <path d="M0,0 L560,0 C400,40 150,130 40,320 L0,320 Z" fill="url(#backSwoosh)"/>
      <path d="M0,0 L520,0 C360,40 130,130 20,320 L0,320 Z" fill="var(--brand-blue)"/>
    </svg>
    <div class="wordmark">Tarrow<br>Construct Works</div>

    <div class="person">
      <p class="person__name">NAME, SURNAME</p>
      <p class="person__role">position</p>
    </div>

    <ul class="contacts">
      <li class="contacts__item">
        <span class="contacts__icon">
          <svg viewBox="0 0 24 24"><path fill="#fff" d="M6.6 10.8a15 15 0 0 0 6.6 6.6l2.2-2.2a1 1 0 0 1 1-.25 11.4 11.4 0 0 0 3.6.57 1 1 0 0 1 1 1V20a1 1 0 0 1-1 1A17 17 0 0 1 3 4a1 1 0 0 1 1-1h3.5a1 1 0 0 1 1 1c0 1.25.2 2.45.57 3.57a1 1 0 0 1-.25 1z"/></svg>
        </span>
        0472 913 046
      </li>
      <li class="contacts__item">
        <span class="contacts__icon">
          <svg viewBox="0 0 24 24"><circle cx="12" cy="12" r="4" fill="none" stroke="#fff" stroke-width="2.4"/><path d="M16 8v5a3 3 0 0 0 5-1 9 9 0 1 0-4 7" fill="none" stroke="#fff" stroke-width="2.4"/></svg>
        </span>
        admin@tarrowconstructworks.com.au
      </li>
      <li class="contacts__item">
        <span class="contacts__icon">
          <svg viewBox="0 0 24 24"><circle cx="12" cy="12" r="9" fill="none" stroke="#fff" stroke-width="2"/><ellipse cx="12" cy="12" rx="4" ry="9" fill="none" stroke="#fff" stroke-width="2"/><path d="M3 12h18" stroke="#fff" stroke-width="2"/></svg>
        </span>
        www.tarrowconstructworks.com.au
      </li>
    </ul>
  </section>

</main>
</body>
</html>
```